Ardenwell Building and Property Services needs a business card design

We need a business card design for our building and property services business. We already have a logo we just need a creative design and layout on a business card. Emphasis on clean, modern, professional.
Our client targets are mainly body corporates, building managers, construction managers.
We are a building services company that lean more to structural repair of buildings, through concrete rectification and carbon fibre strengthening.
We also refurbish facades, rendering, painting etc
We target higher end body corporates in prestigious locations, hence why we'd like our cards to reflect professionalism, strength, efficiency

Target Market(s)

body corporates, building managers, construction managers

Industry/Entity Type

Construction

Contact Information for Business Card

Ardenwell is the main word, with 'Building and Property Services' underneath.
Level 17, 82 Harlow Street
MERRIDALE
Melbourne
Vic 3094
T: 9518 2736
Duncan Ferris - Director
dunardenwell@mailbox-example.com

Requirements
Must have
• Stand out on the back of the card- strong/ bold, company logo
• All of the contact details written above
Should not have
• I'd like the card to stand out, especially on the back. Id like the company logo to be prominent, although feel free to be creative around it. But remain clean and professional

```html
<!DOCTYPE html>
<html lang="en">
<head>
<meta charset="utf-8">
<title>Ardenwell Building and Property Services – Business Card</title>
<link rel="stylesheet" href="https://fonts.googleapis.com/css2?family=Cinzel:wght@500&family=PT+Sans:wght@400&display=swap">
<style>
  :root {
    --page: #e4e2de;
    --card-dark: #0d0f12;
    --card-mid: #1c2026;
    --brand-blue: #2f9fe0;
    --brand-blue-deep: #1677b8;
    --band-light: #5cc4f2;
    --silver: #c9ced4;
    --text-light: #f2f4f6;
    --text-muted: #9aa3ad;
  }
  * { box-sizing: border-box; margin: 0; padding: 0; }
  html, body { width: 1200px; height: 843px; overflow: hidden; }
  body {
    background: var(--page);
    position: relative;
    font-family: "PT Sans", Arial, sans-serif;
  }
  .card {
    position: absolute;
    top: 270px;
    width: 530px;
    height: 303px;
    border-radius: 4px;
    overflow: hidden;
    box-shadow: 0 10px 28px rgba(0,0,0,.28);
  }
  .card-back { left: 46px; }
  .card-front { left: 622px; }

  .surface {
    position: absolute; inset: 0;
    background: radial-gradient(ellipse at 45% 40%, var(--card-mid) 0%, var(--card-dark) 75%);
  }

  .brand-mark {
    display: inline-block;
    width: 14px; height: 14px;
    background: var(--brand-blue);
    margin-right: 10px;
    vertical-align: middle;
  }
  .brand-name {
    font-family: "Cinzel", Georgia, serif;
    font-weight: 500;
    color: var(--brand-blue);
    letter-spacing: 2px;
    vertical-align: middle;
  }
  .brand-tagline {
    font-family: "Cinzel", Georgia, serif;
    font-weight: 500;
    color: var(--brand-blue);
    letter-spacing: 1px;
    text-transform: uppercase;
  }

  /* back */
  .card-back .brand {
    position: absolute;
    left: 0; right: 0; top: 120px;
    text-align: center;
  }
  .card-back .brand-name { font-size: 34px; }
  .card-back .brand-tagline { font-size: 9px; margin-top: 8px; }

  /* front */
  .card-front .brand {
    position: absolute;
    left: 28px; top: 104px;
    width: 200px;
    text-align: center;
  }
  .card-front .brand-name { font-size: 23px; letter-spacing: 1.5px; }
  .card-front .brand-tagline { font-size: 6.5px; margin-top: 6px; }

  .contact {
    position: absolute;
    left: 262px; top: 44px;
    color: var(--text-light);
  }
  .contact-person {
    border-left: 4px solid var(--brand-blue);
    padding-left: 8px;
    margin-left: -12px;
  }
  .contact-name {
    font-family: "Cinzel", Georgia, serif;
    font-weight: 500;
    font-size: 17px;
    color: var(--brand-blue);
    letter-spacing: 1px;
    line-height: 1.1;
  }
  .contact-role {
    font-family: "Cinzel", Georgia, serif;
    font-weight: 500;
    font-size: 12px;
    color: var(--text-light);
    letter-spacing: 1px;
  }
  .contact-address {
    margin-top: 10px;
    font-size: 12.5px;
    line-height: 1.25;
  }
  .contact-lines { list-style: none; margin-top: 6px; font-size: 12.5px; line-height: 1.45; }
  .contact-lines li { display: flex; align-items: center; }
  .contact-lines svg { width: 11px; height: 11px; margin-right: 7px; flex: none; fill: var(--brand-blue); }

  .footer-rule {
    position: absolute; left: 0; right: 0; bottom: 38px; height: 3px;
    background: linear-gradient(90deg, #8d949c, var(--silver), #8d949c);
  }
  .footer-band {
    position: absolute; left: 0; right: 0; bottom: 0; height: 38px;
    background: linear-gradient(180deg, var(--band-light), var(--brand-blue-deep));
  }
</style>
</head>
<body>

<section class="card card-back" aria-label="Card back">
  <div class="surface" role="img" aria-label="Dark perforated metal surface with faint repeating pattern"></div>
  <div class="brand">
    <span class="brand-mark"></span><span class="brand-name">ARDENWELL</span>
    <p class="brand-tagline">Building and Property Services</p>
  </div>
</section>

<section class="card card-front" aria-label="Card front">
  <div class="surface" role="img" aria-label="Dark perforated metal surface"></div>

  <div class="brand">
    <span class="brand-mark"></span><span class="brand-name">ARDENWELL</span>
    <p class="brand-tagline">Building and Property Services</p>
  </div>

  <div class="contact">
    <div class="contact-person">
      <p class="contact-name">DUNCAN FERRIS</p>
      <p class="contact-role">DIRECTOR</p>
    </div>
    <p class="contact-address">Level 17, 82 Harlow Street<br>MERRIDALE, Melbourne<br>Vic 3094</p>
    <ul class="contact-lines">
      <li>
        <svg viewBox="0 0 24 24" aria-hidden="true"><path d="M6.6 10.8a15.1 15.1 0 0 0 6.6 6.6l2.2-2.2a1 1 0 0 1 1-.25 11.4 11.4 0 0 0 3.6.57 1 1 0 0 1 1 1V20a1 1 0 0 1-1 1A17 17 0 0 1 3 4a1 1 0 0 1 1-1h3.5a1 1 0 0 1 1 1c0 1.25.2 2.45.57 3.57a1 1 0 0 1-.25 1z"/></svg>
        9518 2736
      </li>
      <li>
        <svg viewBox="0 0 24 24" aria-hidden="true"><path d="M2 5h20v14H2zM4 7v.5l8 5 8-5V7l-8 5z"/></svg>
        dunardenwell@mailbox-example.com
      </li>
      <li>
        <svg viewBox="0 0 24 24" aria-hidden="true"><circle cx="12" cy="12" r="10"/><path d="M2 12h20M12 2c3 3 3 17 0 20M12 2c-3 3-3 17 0 20" stroke="#0d0f12" stroke-width="1.6" fill="none"/></svg>
        www.ardenwell-example.com
      </li>
    </ul>
  </div>

  <div class="footer-rule"></div>
  <div class="footer-band"></div>
</section>

</body>
</html>
```